IT company requires website redesign

I have an old boring website that I want to update - www.tvkb-example.net
I am a growing IT company beginning to look after more healthcare professionals such as medical and dental practices so a more professional look is required

Blue and orange are the company colours. See one of our local competitors for your reference and ideas - https://www.plinth-halvard.example.au

Target Market(s)

Medical, dental, professional, solicitors etc

Industry/Entity Type

It Support

Number of Pages Required

5+ page

Colors

Designer to choose colors to be used in the design.

Requirements
Must have
• Classy feel, simple with the 'less is more' approach
• On support page, links to support items, a couple more to come
• Reference to our technology partners
• Easy to read
Nice to have
• Company colours are blue with a little orange but I willing to consider new web colour schemes
• leave the rest to you

```html
<!DOCTYPE html>
<html lang="en">
<head>
<meta charset="utf-8">
<title>Meridian Techworks – IT Support</title>
<link href="https://fonts.googleapis.com/css2?family=Exo+2:wght@400;600;700;800&family=Open+Sans:wght@400;600;700&display=swap" rel="stylesheet">
<style>
:root{
  --orange:#e8692a;
  --orange-dark:#d8561c;
  --navy:#0f1a4a;
  --navy-mid:#1e2f7a;
  --ink:#222a3a;
  --muted:#7a8094;
  --line:#e4e8f2;
  --pale:#f4f7fc;
  --white:#ffffff;
}
*{margin:0;padding:0;box-sizing:border-box}
html,body{width:1200px;height:3689px;overflow:hidden}
body{position:relative;font-family:"Open Sans",Arial,sans-serif;color:var(--ink);background:var(--white)}
.abs{position:absolute}
h1,h2,h3,.display{font-family:"Exo 2",Arial,sans-serif}

/* hero */
.hero{left:0;top:0;width:1200px;height:504px;overflow:hidden;
  background:linear-gradient(100deg,#3b3f52 0%,#6e5f58 40%,#b69c88 70%,#8b7568 100%)}
.hero-shade{left:0;top:0;width:1200px;height:504px;background:linear-gradient(90deg,rgba(20,22,40,.55),rgba(20,22,40,.1) 60%)}
.hero-wedge{left:0;top:0}
.brand{left:246px;top:22px;font-family:"Exo 2",sans-serif;font-weight:700;font-size:22px;color:var(--white);display:flex;align-items:center;gap:8px}
.brand-dot{width:12px;height:12px;border-radius:50%;background:var(--orange)}
.nav{right:250px;top:30px;display:flex;gap:22px;font-family:"Exo 2",sans-serif;font-weight:600;font-size:12px;color:var(--white);text-transform:uppercase}
.hero-title{left:248px;top:180px;font-weight:800;font-size:40px;line-height:40px;color:var(--white);text-transform:uppercase}
.hero-sub{left:248px;top:304px;font-size:13px;color:var(--white);text-transform:uppercase;line-height:19px;width:360px}
.btn{display:flex;align-items:center;justify-content:center;border-radius:20px;font-family:"Exo 2",sans-serif;font-weight:700;font-size:11px;text-transform:uppercase}
.btn-orange{background:var(--orange);color:var(--white)}
.btn-white{background:var(--white);color:var(--orange)}

/* section titles */
.section-title{width:1200px;left:0;text-align:center;font-weight:800;font-size:28px;color:var(--orange);text-transform:uppercase}

/* services */
.service{width:167px;height:211px;border-radius:14px;background:var(--white);
  box-shadow:0 4px 18px rgba(40,70,160,.18);text-align:center;padding:36px 10px 0}
.service svg{display:block;margin:0 auto 16px}
.service h3{font-size:11px;font-weight:700;text-transform:uppercase;color:var(--ink);margin-bottom:8px;white-space:nowrap}
.service p{font-size:8.5px;line-height:13px;color:var(--muted)}

/* about */
.about{left:0;top:1126px;width:1200px;height:472px;background:var(--pale)}
.about-title{left:248px;top:1184px;font-weight:800;font-size:27px;line-height:32px;text-transform:uppercase;color:var(--orange)}
.about-list{left:248px;top:1262px;width:380px;list-style:none}
.about-list li{display:flex;gap:12px;font-size:9.5px;line-height:14px;color:#4a5064;margin-bottom:18px}
.about-list svg{flex:none;margin-top:1px}
.about-photo{left:659px;top:1212px;width:337px;height:325px;border-radius:30px 6px 30px 6px;
  background:linear-gradient(135deg,#c9d4e3,#7d8ea8 55%,#2f3c5a)}

/* team */
.team-bg{left:0;top:1598px}
.team-kicker{left:0;width:1200px;top:1708px;text-align:center;color:var(--white);font-family:"Exo 2",sans-serif;font-weight:700;font-size:12px;text-transform:uppercase}
.team-title{left:0;width:1200px;top:1724px;text-align:center;color:var(--white);font-weight:800;font-size:27px;text-transform:uppercase}
.member{width:167px;height:241px;background:linear-gradient(180deg,#2a3e9a,#1a2a72);text-align:center;padding-top:28px;color:var(--white)}
.member .portrait{width:108px;height:108px;border-radius:50%;margin:0 auto 18px;border:4px solid var(--white);
  background:linear-gradient(160deg,#c6b0a2,#6c5a52)}
.member h3{font-size:13px;font-weight:700;text-transform:uppercase}
.member p{font-size:8.5px;margin-top:2px;opacity:.9}
.member .social{display:flex;justify-content:center;gap:10px;margin-top:12px}
.member .social span{width:7px;height:7px;border-radius:50%;background:var(--white)}

/* testimonials */
.quote{width:338px;height:162px;border-radius:22px;padding:22px 24px}
.quote-light{background:var(--white);box-shadow:0 4px 18px rgba(40,70,160,.15)}
.quote-orange{background:var(--orange);color:var(--white)}
.quote .mark{font-family:"Exo 2",sans-serif;font-weight:800;font-size:44px;line-height:30px;float:left;margin-right:10px}
.quote-light .mark{color:var(--orange)}
.quote .text{font-size:8.5px;line-height:13px}
.quote-light .text{color:var(--muted)}
.quote .who{display:flex;align-items:center;gap:10px;margin-top:22px;clear:both}
.quote .avatar{width:32px;height:32px;border-radius:50%;background:linear-gradient(160deg,#c9b3a4,#6d5c54)}
.quote .name{font-size:9px;font-weight:700}
.quote-light .name{color:var(--orange)}
.quote .role{font-size:8px}

/* cta */
.cta{left:0;top:2582px;width:1200px;height:226px;background:linear-gradient(90deg,#c88a66 0%,var(--orange) 45%,var(--orange-dark) 100%)}
.cta-photo{left:0;top:2582px;width:460px;height:226px;background:linear-gradient(90deg,rgba(120,100,95,.75),rgba(232,105,42,0))}
.cta-title{left:0;width:1200px;top:2628px;text-align:center;color:var(--white);font-weight:800;font-size:27px;line-height:31px;text-transform:uppercase}
.cta-sub{left:0;width:1200px;top:2692px;text-align:center;color:var(--white);font-size:9.5px}

/* partners */
.partners-sub{left:0;width:1200px;top:2905px;text-align:center;font-size:16px;line-height:22px;color:#3a4052}
.partner{width:124px;height:88px;border:1px solid var(--line);background:var(--white);display:flex;align-items:center;justify-content:center}
.partner span{display:block;width:70px;height:34px;border-radius:6px}

/* footer */
.footer{left:0;top:3246px;width:1200px;height:443px;background:radial-gradient(ellipse at 60% 40%,#1c2a6b,var(--navy) 70%)}
.footer-heading{font-family:"Exo 2",sans-serif;font-size:18px;font-weight:800;color:var(--white);text-transform:uppercase}
.footer-label{font-family:"Exo 2",sans-serif;font-weight:700;font-size:12px;color:var(--white);text-transform:uppercase}
.contact-line{display:flex;align-items:center;gap:12px;font-size:9.5px;color:var(--white);margin-bottom:14px}
.links{display:grid;grid-template-columns:100px 100px;row-gap:8px;font-size:9px;color:var(--white)}
.links span::before{content:"•";margin-right:6px;color:var(--white)}
.field{border:1px solid rgba(255,255,255,.15);background:rgba(255,255,255,.03);color:rgba(255,255,255,.8);font-size:9px;padding:12px 14px}
.send{background:var(--white);display:flex;align-items:center;justify-content:center;font-family:"Exo 2",sans-serif;font-weight:700;font-size:11px;color:var(--navy)}
.foot-social{display:flex;gap:10px}
.foot-social span{width:28px;height:28px;border-radius:50%;background:var(--white)}
</style>
</head>
<body>

<!-- HERO -->
<section class="hero abs" role="img" aria-label="Photo of colleagues working together at laptops in a bright office"></section>
<div class="hero-shade abs"></div>
<svg class="hero-wedge abs" width="1200" height="504" viewBox="0 0 1200 504">
  <polygon points="0,280 0,504 300,504" fill="#2b3fb0" opacity=".9"/>
</svg>
<div class="brand abs"><span class="brand-dot"></span>Meridian Techworks</div>
<nav class="nav abs">
  <span>Home</span><span>Our Services</span><span>About Us</span><span>Our Team</span><span>Contact Us</span><span>Support</span>
</nav>
<h1 class="hero-title abs">Welcome to<br>Meridian<br>Techworks!</h1>
<p class="hero-sub abs">A better tomorrow, through intel-<br>ligent use of technology today!</p>
<div class="btn btn-orange abs" style="left:248px;top:364px;width:128px;height:36px">Readmore</div>

<!-- SERVICES -->
<h2 class="section-title abs" style="top:544px">Our Services</h2>

<div class="service abs" style="left:236px;top:620px">
  <svg width="46" height="46" viewBox="0 0 46 46" fill="none" stroke="#2a3e9a" stroke-width="2"><rect x="6" y="8" width="34" height="24" rx="2"/><path d="M16 40h14M23 32v8"/><circle cx="23" cy="20" r="5" stroke="#e8692a"/></svg>
  <h3>Software</h3><p>Our team sources the tools, capabilities and expertise to guide any organisation with their software requirements</p>
</div>
<div class="service abs" style="left:423px;top:620px">
  <svg width="46" height="46" viewBox="0 0 46 46" fill="none" stroke="#2a3e9a" stroke-width="2"><rect x="8" y="10" width="30" height="20" rx="2"/><path d="M4 36h38"/><path d="M18 20l4 4 6-7" stroke="#e8692a"/></svg>
  <h3>Products</h3><p>We can determine and provide appropriate products and services to address your technology requirements</p>
</div>
<div class="service abs" style="left:610px;top:620px">
  <svg width="46" height="46" viewBox="0 0 46 46" fill="none" stroke="#2a3e9a" stroke-width="2"><rect x="6" y="8" width="34" height="24" rx="2"/><path d="M16 40h14M23 32v8"/><path d="M14 24h4v-6h4v-4h4v10h6" stroke="#e8692a"/></svg>
  <h3>Solutions</h3><p>A full range of IT solutions, includes carefully selected IT partners to minimise risk and improve continuity</p>
</div>
<div class="service abs" style="left:797px;top:620px">
  <svg width="46" height="46" viewBox="0 0 46 46" fill="none" stroke="#2a3e9a" stroke-width="2"><rect x="10" y="6" width="20" height="34" rx="3"/><circle cx="32" cy="30" r="8" stroke="#e8692a"/><path d="M16 12h8"/></svg>
  <h3>Finance – Easy Lease</h3><p>Concerned about your budget? We can help you with payment plan options</p>
</div>

<div class="service abs" style="left:236px;top:848px">
  <svg width="46" height="46" viewBox="0 0 46 46" fill="none" stroke="#e8692a" stroke-width="2"><circle cx="17" cy="27" r="8"/><circle cx="17" cy="27" r="3"/><circle cx="32" cy="14" r="6" stroke="#2a3e9a"/><circle cx="32" cy="14" r="2" stroke="#2a3e9a"/></svg>
  <h3>Programming</h3><p>Electronic design manufacturing and microprocessor programming</p>
</div>
<div class="service abs" style="left:423px;top:848px">
  <svg width="46" height="46" viewBox="0 0 46 46" fill="none" stroke="#2a3e9a" stroke-width="2"><path d="M12 6h16l8 8v26H12z"/><path d="M18 20h12M18 26h12M18 32h8" stroke="#e8692a"/></svg>
  <h3>Copiers</h3><p>Office multifunction copiers with full integration into networks for printing and scanning</p>
</div>
<div class="service abs" style="left:610px;top:848px">
  <svg width="46" height="46" viewBox="0 0 46 46" fill="none" stroke="#2a3e9a" stroke-width="2"><rect x="14" y="6" width="18" height="10"/><rect x="6" y="16" width="34" height="16" rx="2"/><rect x="14" y="28" width="18" height="12" stroke="#e8692a"/></svg>
  <h3>Printers &amp; Scanners</h3><p>Colour lasers, inkjet and wide format integration into networks for printing and scanning</p>
</div>
<div class="service abs" style="left:797px;top:848px">
  <svg width="46" height="46" viewBox="0 0 46 46" fill="none" stroke="#2a3e9a" stroke-width="2"><rect x="6" y="8" width="34" height="24" rx="2"/><path d="M16 40h14M23 32v8"/><path d="M14 20h18M23 14v12" stroke="#e8692a"/></svg>
  <h3>Web Hosting and Design</h3><p>Our team of specialised staff are ready and waiting to assist you with all your website design and hosting needs</p>
</div>

<!-- ABOUT -->
<section class="about abs"></section>
<h2 class="about-title abs">About<br>Meridian Techworks</h2>
<ul class="about-list abs">
  <li><svg width="22" height="12" viewBox="0 0 22 12" fill="none" stroke="#2a3e9a" stroke-width="2"><path d="M1 6l4 4 8-9M9 10l1 0 8-9"/></svg>Commenced trading in 1996, the retail division was sold in 2002. That September our company was launched</li>
  <li><svg width="22" height="12" viewBox="0 0 22 12" fill="none" stroke="#2a3e9a" stroke-width="2"><path d="M1 6l4 4 8-9M9 10l1 0 8-9"/></svg>100% Australian owned and operated</li>
  <li><svg width="22" height="12" viewBox="0 0 22 12" fill="none" stroke="#2a3e9a" stroke-width="2"><path d="M1 6l4 4 8-9M9 10l1 0 8-9"/></svg>Coast based company servicing south east Queensland with a 'We come to you' attitude</li>
  <li><svg width="22" height="12" viewBox="0 0 22 12" fill="none" stroke="#2a3e9a" stroke-width="2"><path d="M1 6l4 4 8-9M9 10l1 0 8-9"/></svg>Multi disciplinary service provider for the computer industry</li>
  <li><svg width="22" height="12" viewBox="0 0 22 12" fill="none" stroke="#2a3e9a" stroke-width="2"><path d="M1 6l4 4 8-9M9 10l1 0 8-9"/></svg>Born out of the need for talented and local IT supply, support and services people with a complete understanding of the requirements and peculiarities that is IT</li>
  <li><svg width="22" height="12" viewBox="0 0 22 12" fill="none" stroke="#2a3e9a" stroke-width="2"><path d="M1 6l4 4 8-9M9 10l1 0 8-9"/></svg>Support that does not end 5pm Friday night</li>
  <li><svg width="22" height="12" viewBox="0 0 22 12" fill="none" stroke="#2a3e9a" stroke-width="2"><path d="M1 6l4 4 8-9M9 10l1 0 8-9"/></svg>Collectively provide flexible, complete and cost effective solutions</li>
</ul>
<div class="about-photo abs" role="img" aria-label="Photo of business team reviewing documents together"></div>

<!-- TEAM -->
<svg class="team-bg abs" width="1200" height="627" viewBox="0 0 1200 627">
  <defs>
    <linearGradient id="teamGrad" x1="0" y1="0" x2="0" y2="1">
      <stop offset="0" stop-color="#0f1a4a"/><stop offset="1" stop-color="#25389a"/>
    </linearGradient>
  </defs>
  <path d="M0 40 C150 0 300 70 480 30 C660 -10 820 60 1000 25 C1100 8 1160 30 1200 40 V600 H0Z" fill="#c9cde8"/>
  <path d="M0 55 C160 15 320 85 500 45 C680 5 840 75 1020 40 C1110 22 1170 45 1200 55 V590 C1050 560 900 620 720 595 C540 570 380 620 200 590 C120 578 50 585 0 600Z" fill="url(#teamGrad)"/>
  <path d="M0 600 C50 585 120 578 200 590 C380 620 540 570 720 595 C900 620 1050 560 1200 590 V627 H0Z" fill="#dfe2f2"/>
</svg>
<div class="team-kicker abs">Meet the</div>
<h2 class="team-title abs">Our Team</h2>

<div class="member abs" style="left:251px;top:1795px">
  <div class="portrait" role="img" aria-label="Portrait of team member"></div>
  <h3>Alden Brooke</h3><p>Business Machines</p>
  <div class="social"><span></span><span></span><span></span></div>
</div>
<div class="member abs" style="left:430px;top:1795px">
  <div class="portrait" role="img" aria-label="Portrait of team member" style="background:linear-gradient(160deg,#a9b28a,#55603f)"></div>
  <h3>Corin Maddox</h3><p>Linux &amp; Database Specialist</p>
  <div class="social"><span></span><span></span><span></span></div>
</div>
<div class="member abs" style="left:607px;top:1795px">
  <div class="portrait" role="img" aria-label="Portrait of team member" style="background:linear-gradient(160deg,#c66a4a,#6a2e22)"></div>
  <h3>Tessa Warrick</h3><p>Office Manager</p>
  <div class="social"><span></span><span></span><span></span></div>
</div>
<div class="member abs" style="left:787px;top:1795px">
  <div class="portrait" role="img" aria-label="Portrait of team member" style="background:linear-gradient(160deg,#d8d0c8,#8a7a70)"></div>
  <h3>Nolan Pryce</h3><p>Senior Field Technician</p>
  <div class="social"><span></span><span></span><span></span></div>
</div>
<div class="btn btn-white abs" style="left:534px;top:2085px;width:130px;height:40px;color:var(--navy)">All View More</div>

<!-- TESTIMONIALS -->
<h2 class="section-title abs" style="top:2277px">Testimonials</h2>
<svg class="abs" style="left:192px;top:2408px" width="20" height="34" viewBox="0 0 20 34"><path d="M16 3L4 17l12 14" fill="none" stroke="#e8692a" stroke-width="5"/></svg>
<svg class="abs" style="left:988px;top:2408px" width="20" height="34" viewBox="0 0 20 34"><path d="M4 3l12 14L4 31" fill="none" stroke="#7a8094" stroke-width="5"/></svg>

<div class="quote quote-light abs" style="left:251px;top:2348px">
  <span class="mark">“</span>
  <p class="text">Our team has been our IT support company for over 10 years. So why do we stick with them? Because they are awesome, the staff are consistently able to solve our many and varied problems. Whether we phone about simple functionality</p>
  <div class="who"><div class="avatar" role="img" aria-label="Client portrait"></div><div><div class="name">Owen and Mara Lindell</div><div class="role" style="color:var(--muted)">Owen and Mara Lindell</div></div></div>
</div>
<div class="quote quote-orange abs" style="left:610px;top:2348px">
  <span class="mark">“</span>
  <p class="text">Our team has been our IT support company for over 10 years. So why do we stick with them? Because they are awesome, the staff are consistently able to solve our many and varied problems. Whether we phone about simple functionality.</p>
  <div class="who"><div class="avatar" role="img" aria-label="Client portrait"></div><div><div class="name">Harriet</div><div class="role">ADMINISTRATION MANAGER</div></div></div>
</div>

<!-- CTA -->
<section class="cta abs"></section>
<div class="cta-photo abs" role="img" aria-label="Photo of smiling colleagues gathered around a laptop"></div>
<h2 class="cta-title abs">Meridian Techworks<br><span style="font-weight:600">We are here to help you!</span></h2>
<p class="cta-sub abs">A Better Tomorrow, Through intelligent use of Technology Today!</p>
<div class="btn btn-white abs" style="left:528px;top:2720px;width:130px;height:40px">Contact Us</div>

<!-- PARTNERS -->
<h2 class="section-title abs" style="top:2852px">Some of our partners</h2>
<p class="partners-sub abs">We partner with only the best companies around the world to offer<br>our clients the BEST in Hardware and Software solutions</p>

<div class="partner abs" style="left:251px;top:2988px"><span style="background:#1f5fa8;border-radius:50%;width:44px;height:44px"></span></div>
<div class="partner abs" style="left:394px;top:2988px"><span style="background:#d23a35;height:14px"></span></div>
<div class="partner abs" style="left:537px;top:2988px"><span style="background:#1aa1e6;width:56px;height:56px;border-radius:2px"></span></div>
<div class="partner abs" style="left:680px;top:2988px"><span style="background:#1662b0;width:28px;height:28px;border-radius:50%"></span></div>
<div class="partner abs" style="left:823px;top:2988px"><span style="background:#2b4a8a;height:18px"></span></div>
<div class="partner abs" style="left:251px;top:3093px"><span style="background:#6e8a3a;height:12px"></span></div>
<div class="partner abs" style="left:394px;top:3093px"><span style="background:#2a7ab8;width:52px;height:62px"></span></div>
<div class="partner abs" style="left:537px;top:3093px"><span style="background:#2c2c38;width:40px;height:62px"></span></div>
<div class="partner abs" style="left:680px;top:3093px"><span style="background:#1d3c8c;height:14px"></span></div>
<div class="partner abs" style="left:823px;top:3093px"><span style="background:#333;width:30px;height:36px;border-radius:50% 50% 40% 40%"></span></div>

<!-- FOOTER -->
<footer class="footer abs"></footer>
<h3 class="footer-heading abs" style="left:248px;top:3314px">Contact Us</h3>
<div class="footer-label abs" style="left:248px;top:3352px">Meridian Techworks</div>
<div class="abs" style="left:248px;top:3384px">
  <div class="contact-line"><svg width="18" height="18" viewBox="0 0 24 24" fill="none" stroke="#fff" stroke-width="2"><path d="M5 3h4l2 5-3 2a12 12 0 006 6l2-3 5 2v4a2 2 0 01-2 2A18 18 0 013 5a2 2 0 012-2z"/></svg>1800 000 417</div>
  <div class="contact-line"><svg width="18" height="18" viewBox="0 0 24 24" fill="none" stroke="#fff" stroke-width="2"><rect x="3" y="5" width="18" height="14"/><path d="M3 5l9 8 9-8"/></svg>info@tvkb-example.net</div>
  <div class="contact-line"><svg width="18" height="18" viewBox="0 0 24 24" fill="none" stroke="#fff" stroke-width="2"><circle cx="12" cy="12" r="9"/><path d="M3 12h18M12 3c4 4 4 14 0 18M12 3c-4 4-4 14 0 18"/></svg>12 Example Rd, Seaview QLD 4000</div>
</div>
<div class="footer-label abs" style="left:248px;top:3496px">Quick Links</div>
<div class="links abs" style="left:252px;top:3522px">
  <span>Home</span><span>Our Services</span><span>About us</span><span>Support</span><span>Our Team</span><span>Contact us</span>
</div>

<h3 class="footer-heading abs" style="left:492px;top:3314px">Get in touch now</h3>
<div class="field abs" style="left:492px;top:3361px;width:222px;height:37px">Name</div>
<div class="field abs" style="left:725px;top:3361px;width:222px;height:37px">Email</div>
<div class="field abs" style="left:492px;top:3411px;width:455px;height:37px">Phone</div>
<div class="field abs" style="left:492px;top:3460px;width:455px;height:81px">Messages</div>
<div class="send abs" style="left:492px;top:3561px;width:101px;height:37px">SEND</div>

<div class="abs" style="left:248px;top:3646px;font-size:9px;color:var(--white)">Copyright © 2019 <b>Meridian Techworks</b> All Right Reserved</div>
<div class="foot-social abs" style="left:806px;top:3636px"><span></span><span></span><span></span><span></span></div>

</body>
</html>
```